Update Wordpress website to be captivating, modern and concise

Help us create a cohesive brand and deliver our marketing messages more concisely. We would like to update our Wordpress website to be clean, modern and captivating. Please see the uploaded file for more information on our company, our current website and how we want to continue the relationship beyond the contest. Thank you and we look forward to receiving your creative ideas!

Update: We no longer need you to complete the development.
Updates

We no longer require you to implement the design in Wordpress. Please provide your best, creative designs. Thanks

Target Market(s)

Our customers are companies who are looking for sleek, sexy, easy to use mobile applications for their sales teams. Our customers range from your small to Zenlow 300.

Industry/Entity Type

Marketing

Font styles to use
Sans Serif

Requirements
Must have
• Clean, contemporary, engaging. Comes across as easy to use and inviting. Use the blue in our logo. We do a lot of work on Quorvel Apps and therefore our standard is the Quorvel UX for our styling and UI.
Should not have
• Clutter and distracting.

```html
<!DOCTYPE html>
<html lang="en">
<head>
<meta charset="utf-8">
<title>Fluxbase Analytics</title>
<link rel="stylesheet" href="https://fonts.googleapis.com/css2?family=Open+Sans:wght@400;600&family=Roboto:wght@400;500&family=Roboto+Condensed:wght@400&display=swap">
<style>
:root{
  --blue:#1f6fd2;
  --blue-light:#6fb0f4;
  --ink:#2a2a2a;
  --muted:#555;
  --line:#e3e3e3;
  --band:#eeeeee;
  --footer:#222222;
  --footer-text:#a9a9a9;
  --white:#fff;
}
*{box-sizing:border-box;margin:0;padding:0}
html,body{width:1200px;height:2365px;overflow:hidden}
body{font-family:"Open Sans",Arial,sans-serif;color:var(--ink);background:var(--white);position:relative}
.wrap{position:absolute;left:98px;width:1004px}
h2,h3,h4{font-family:"Roboto",Arial,sans-serif;font-weight:400}

/* top bar */
.topbar{position:absolute;top:0;left:0;width:1200px;height:43px;background:#f7f7f7;border-bottom:1px solid var(--line);font-size:12px}
.topbar .follow{position:absolute;left:98px;top:14px;color:var(--blue);font-size:12px}
.topbar .dots{position:absolute;left:182px;top:15px;display:flex;gap:22px}
.topbar .dots span{width:12px;height:12px;border-radius:50%;background:#b9b9b9;display:block}
.topbar .contact{position:absolute;right:98px;top:13px;display:flex;gap:36px;color:#444}
.topbar .contact svg{vertical-align:-3px;margin-right:8px}

/* header */
.header{position:absolute;top:43px;left:0;width:1200px;height:107px;border-bottom:1px solid var(--line)}
.brand{position:absolute;left:98px;top:30px;display:flex;align-items:center;gap:10px;font-family:"Roboto",Arial,sans-serif;font-size:24px;font-weight:500;color:#333}
.brand .mark{width:40px;height:40px;border-radius:50%;background:var(--blue)}
.nav{position:absolute;right:98px;top:44px;display:flex;gap:38px;font-size:13px;color:#333;letter-spacing:.2px}

/* hero */
.hero{position:absolute;top:150px;left:0;width:1200px;height:517px;background:linear-gradient(100deg,#e9eef2 0%,#c7d3dc 30%,#5f7f99 55%,#3f6584 75%,#6d8aa3 100%)}
.hero .arrow{position:absolute;top:241px;width:34px;height:34px;border-radius:50%;background:rgba(0,0,0,.35)}
.hero .arrow.left{left:34px}.hero .arrow.right{right:34px}
.hero .arrow svg{position:absolute;left:11px;top:10px}
.caption{position:absolute;left:683px;font-family:"Roboto Condensed",Arial,sans-serif;color:#fff;background:rgba(40,40,40,.82);padding:0 16px}
.caption.one{top:183px;height:66px;line-height:66px;font-size:33px}
.caption.two{top:257px;height:66px;line-height:66px;font-size:35px}

/* features */
.features-title{position:absolute;top:692px;left:0;width:1200px;text-align:center;font-size:26px;color:#333}
.features{top:760px;display:flex;justify-content:space-between}
.feature{width:218px;text-align:center}
.ring{position:relative;width:140px;height:148px;margin:0 auto}
.ring .shadow{position:absolute;left:30px;bottom:0;width:80px;height:8px;border-radius:50%;background:radial-gradient(#dcdcdc,transparent 70%)}
.feature h3{margin-top:20px;font-size:16px;color:var(--blue)}
.feature p{margin-top:14px;font-size:11.5px;line-height:20px;color:#444}
.feature .more{display:block;margin-top:14px;font-size:14px;color:#222}
.feature .more b{color:var(--blue);font-weight:400;margin-left:6px}

/* cta band */
.cta{position:absolute;top:1088px;left:0;width:1200px;height:100px;background:var(--band);border-top:1px solid var(--line);border-bottom:1px solid var(--line)}
.cta h2{position:absolute;left:98px;top:32px;font-size:26px;color:#222}
.cta .btn{position:absolute;right:98px;top:29px;width:172px;height:44px;border-radius:22px;background:var(--blue);color:#fff;font-size:14px;text-align:center;line-height:44px;letter-spacing:.3px}

/* info columns */
.col-title{position:absolute;top:1232px;font-size:18px;color:#222;padding-bottom:12px;border-bottom:1px solid var(--line)}
.articles-nav{position:absolute;left:562px;top:1234px;font-size:16px;color:#333}
.article{position:absolute;top:1301px;width:233px}
.article .photo{height:158px}
.article h4{margin-top:18px;font-size:15.5px;color:#222}
.article p{margin-top:14px;font-size:11px;line-height:20px;color:#444}
.article .meta{margin-top:18px;padding-top:12px;border-top:1px solid var(--line);display:flex;justify-content:space-between;font-size:10.5px;color:#222}
.accordion{position:absolute;left:612px;top:1300px;width:232px}
.acc-item{border:1px solid var(--line);height:37px;margin-bottom:6px;padding:0 14px;display:flex;justify-content:space-between;align-items:center;font-size:12px;color:#222}
.acc-open{border:1px solid var(--line);margin-bottom:6px;padding:0 14px 14px}
.acc-open .head{height:37px;display:flex;justify-content:space-between;align-items:center;color:var(--blue);font-size:12px}
.acc-open p{font-size:10.5px;line-height:20px;color:#333}
.skills{position:absolute;left:869px;top:1300px;width:233px}
.skill{position:relative;height:46px;margin-bottom:6px;border:1px solid var(--line);background:#fafafa}
.skill .bar{position:absolute;left:0;top:0;height:100%;background:var(--blue);color:#fff;font-size:12.5px;line-height:46px;padding-left:16px}
.skill .pct{position:absolute;right:18px;top:0;line-height:46px;font-size:12.5px;color:var(--blue)}

/* testimonials */
.testimonials{position:absolute;top:1680px;left:0;width:1200px;height:212px;background:var(--band)}
.testimonials h2{text-align:center;margin-top:24px;font-size:27px;color:#333}
.testimonials p{width:860px;margin:18px auto 0;text-align:center;font-size:12px;line-height:24px;color:#444}
.testimonials .q{position:absolute;font-family:Georgia,serif;font-size:30px;color:var(--blue)}
.testimonials .who{text-align:center;margin-top:14px;font-size:16px;color:#222}
.testimonials .who span{color:var(--blue)}

/* partners */
.partners{top:1940px;display:flex;justify-content:space-between;align-items:center;padding:0 30px}
.partner{display:flex;align-items:center;gap:8px;font-size:19px;font-weight:600;color:#555}
.partner i{width:18px;height:18px;border-radius:50%;background:#999;display:block}

/* footer */
.footer{position:absolute;top:2023px;left:0;width:1200px;height:282px;background:var(--footer);color:var(--footer-text)}
.fcol{position:absolute;top:32px}
.fcol h4{font-size:17px;color:#fff;letter-spacing:.4px;margin-bottom:18px}
.fcol p{font-size:11.5px;line-height:21px}
.newsletter form{display:flex;margin-top:18px}
.newsletter .field{width:155px;height:42px;background:#2c2c2c;font-size:11px;color:#666;line-height:42px;padding-left:14px}
.newsletter .send{width:78px;height:42px;background:var(--blue);color:#fff;font-size:15px;text-align:center;line-height:42px}
.tweet{display:flex;gap:14px;margin-bottom:16px}
.tweet i{flex:0 0 16px;height:16px;background:#fff;border-radius:2px;margin-top:3px}
.contact-list li{list-style:none;display:flex;gap:14px;font-size:12px;line-height:21px;margin-bottom:16px}
.social li{list-style:none;display:flex;align-items:center;gap:12px;font-size:12px;margin-bottom:11px}
.social li i{width:8px;height:8px;border-radius:50%;background:#aaa;display:block}
.bottombar{position:absolute;top:2305px;left:0;width:1200px;height:60px;background:var(--blue);color:#fff;text-align:center;line-height:60px;font-size:11.5px}
</style>
</head>
<body>

<div class="topbar">
  <span class="follow">FOLLOW US</span>
  <div class="dots"><span></span><span></span><span></span><span></span></div>
  <div class="contact">
    <span><svg width="14" height="14" viewBox="0 0 24 24"><path fill="#666" d="M6.6 10.8a15 15 0 0 0 6.6 6.6l2.2-2.2c.3-.3.7-.4 1-.2 1.1.4 2.3.6 3.6.6.6 0 1 .4 1 1V20c0 .6-.4 1-1 1A17 17 0 0 1 3 4c0-.6.4-1 1-1h3.5c.6 0 1 .4 1 1 0 1.3.2 2.5.6 3.6.1.3 0 .7-.2 1z"/></svg>CALL US: 1-555-014-2290</span>
    <span><svg width="14" height="12" viewBox="0 0 24 18"><rect x="1" y="1" width="22" height="16" fill="none" stroke="#666" stroke-width="2"/><path d="M1 1l11 9 11-9" fill="none" stroke="#666" stroke-width="2"/></svg>hello@fluxbase.example</span>
  </div>
</div>

<header class="header">
  <div class="brand"><span class="mark"></span>Fluxbase Analytics</div>
  <nav class="nav"><span>HOME</span><span>ABOUT US</span><span>PROJECTS</span><span>JOIN THE TEAM</span><span>BLOG</span><span>CONTACT US</span></nav>
</header>

<section class="hero" role="img" aria-label="Photo of a businessman looking through binoculars against a cloudy sky with handwritten business words">
  <span class="arrow left"><svg width="12" height="14" viewBox="0 0 12 14"><path d="M9 1L3 7l6 6" stroke="#fff" stroke-width="2" fill="none"/></svg></span>
  <span class="arrow right"><svg width="12" height="14" viewBox="0 0 12 14"><path d="M3 1l6 6-6 6" stroke="#fff" stroke-width="2" fill="none"/></svg></span>
  <div class="caption one">FLUXBASE ANALYTICS</div>
  <div class="caption two">Where Mobility Meets Big Data</div>
</section>

<h2 class="features-title">Top 20 Most Promising Data Analytics Company</h2>
<div class="wrap features" style="position:absolute">
  <div class="feature">
    <div class="ring"><svg width="140" height="140" viewBox="0 0 140 140"><circle cx="70" cy="70" r="62" fill="none" stroke="var(--blue)" stroke-width="10"/><path d="M14 44A62 62 0 0 1 70 8" fill="none" stroke="var(--blue-light)" stroke-width="10"/><path d="M52 58h4l5 18h18l4-13H58" fill="none" stroke="#222" stroke-width="4"/><circle cx="63" cy="83" r="3" fill="#222"/><circle cx="77" cy="83" r="3" fill="#222"/></svg><span class="shadow"></span></div>
    <h3>Order Management</h3>
    <p>Lorem ipsum dolor sit amet, consectetur adipiscing elit, sed do eiusmod tempor Lorem ipsum dolor sit amet,</p>
    <span class="more">Discover<b>&gt;</b></span>
  </div>
  <div class="feature">
    <div class="ring"><svg width="140" height="140" viewBox="0 0 140 140"><circle cx="70" cy="70" r="62" fill="none" stroke="var(--blue)" stroke-width="10"/><path d="M14 44A62 62 0 0 1 70 8" fill="none" stroke="var(--blue-light)" stroke-width="10"/><path d="M88 52L52 68l14 4 4 14z" fill="#222"/></svg><span class="shadow"></span></div>
    <h3>Goal Manager</h3>
    <p>Lorem ipsum dolor sit amet, consectetur adipiscing elit, sed do eiusmod tempor Lorem ipsum dolor sit amet,</p>
    <span class="more">Discover<b>&gt;</b></span>
  </div>
  <div class="feature">
    <div class="ring"><svg width="140" height="140" viewBox="0 0 140 140"><circle cx="70" cy="70" r="62" fill="none" stroke="var(--blue)" stroke-width="10"/><path d="M14 44A62 62 0 0 1 70 8" fill="none" stroke="var(--blue-light)" stroke-width="10"/><path d="M65 54l-4 32M79 54l-4 32M56 64h32M52 76h32" stroke="#222" stroke-width="5"/></svg><span class="shadow"></span></div>
    <h3>Sales Enablement</h3>
    <p>Lorem ipsum dolor sit amet, consectetur adipiscing elit, sed do eiusmod tempor Lorem ipsum dolor sit amet,</p>
    <span class="more">Discover<b>&gt;</b></span>
  </div>
  <div class="feature">
    <div class="ring"><svg width="140" height="140" viewBox="0 0 140 140"><circle cx="70" cy="70" r="62" fill="none" stroke="var(--blue)" stroke-width="10"/><path d="M14 44A62 62 0 0 1 70 8" fill="none" stroke="var(--blue-light)" stroke-width="10"/><rect x="60" y="50" width="20" height="38" rx="3" fill="none" stroke="#222" stroke-width="4"/><circle cx="70" cy="82" r="2" fill="#222"/></svg><span class="shadow"></span></div>
    <h3>Mobile Solutions</h3>
    <p>Lorem ipsum dolor sit amet, consectetur adipiscing elit, sed do eiusmod tempor Lorem ipsum dolor sit amet,</p>
    <span class="more">Discover<b>&gt;</b></span>
  </div>
</div>

<section class="cta">
  <h2>Wins Wholesale Industry Solutions App Challenge</h2>
  <span class="btn">JOIN THE TEAM</span>
</section>

<h2 class="col-title" style="left:98px">Latest Articles</h2>
<span class="articles-nav">&lsaquo; &rsaquo;</span>
<h2 class="col-title" style="left:612px">More About us</h2>
<h2 class="col-title" style="left:869px">Our Capabilities</h2>

<article class="article" style="left:98px">
  <div class="photo" role="img" aria-label="Photo of a hand holding a smartphone near a printer" style="background:linear-gradient(135deg,#f2f2f2,#c9c9c9 60%,#6c6c6c)"></div>
  <h4>What do you need to know?</h4>
  <p>Its Finally Here! Its easy to overlook the challenges in upgrading an existing install base to a new version...</p>
  <div class="meta"><span>SEPTEMBER 17, 2014</span><span>&#9675; 0 &nbsp; &#9825; 1</span></div>
</article>
<article class="article" style="left:356px">
  <div class="photo" role="img" aria-label="Photo of a woman presenting floating cloud and device icons" style="background:linear-gradient(135deg,#e8f1f8,#a9c8e0 60%,#6f8fa8)"></div>
  <h4>Partner Portal Launch!</h4>
  <p>Its Finally Here! Its easy to overlook the challenges in upgrading an existing install base to a new version...</p>
  <div class="meta"><span>AUGUST 17, 2014</span><span>&#9675; 0 &nbsp; &#9825; 2</span></div>
</article>

<div class="accordion">
  <div class="acc-open">
    <div class="head"><span>Ravi Solenko</span><span>&minus;</span></div>
    <p>Ravi is President and CEO and Chief Data Scientist of Fluxbase Analytics. Fluxbase Analytics is where "Insightful analytics meet inspiring user experiences." With over 30 years of experience,</p>
  </div>
  <div class="acc-item"><span>Corbin Ashford</span><b>+</b></div>
  <div class="acc-item"><span>Maren Tolliver</span><b>+</b></div>
  <div class="acc-item"><span>Dario Pemberly</span><b>+</b></div>
  <div class="acc-item"><span>Lina Varga</span><b>+</b></div>
</div>

<div class="skills">
  <div class="skill"><span class="bar" style="width:171px">Wholesale Distribution</span><span class="pct">75%</span></div>
  <div class="skill"><span class="bar" style="width:145px">Solution Selling</span><span class="pct">60%</span></div>
  <div class="skill"><span class="bar" style="width:124px">Capacity Planning</span><span class="pct">50%</span></div>
  <div class="skill"><span class="bar" style="width:163px">Mobile Solutions</span><span class="pct">95%</span></div>
  <div class="skill"><span class="bar" style="width:144px">Marketing</span><span class="pct">75%</span></div>
  <div class="skill"><span class="bar" style="width:180px">Project Management</span><span class="pct">90%</span></div>
</div>

<section class="testimonials">
  <h2>Testimonials</h2>
  <span class="q" style="left:144px;top:64px">&ldquo;</span>
  <p>Lorem ipsum dolor sit amet, consectetur adipiscing elit. Sed blandit massa vel mauris sollicitudin dignissim. Phasellus ultrices tellus eget ipsum ornare molestie scelerisque eros dignissim. Phasellus fringilla hendrerit lectus nec vehicula. Pellentesque habitant morbi tristique senectus et netus et malesuada fames ac turpis egestas. Lorem ipsum dolor sit amet, consectetur adipiscing elit. Sed blandit massa</p>
  <span class="q" style="left:1030px;top:138px">&rdquo;</span>
  <div class="who"><span>Tobias Lindqvist</span> , Sitegrove</div>
</section>

<div class="wrap partners" style="position:absolute">
  <span class="partner"><i></i>Heron</span>
  <span class="partner">Pelicor</span>
  <span class="partner"><i></i>Stackmint</span>
  <span class="partner"><i></i>Loopwise</span>
  <span class="partner">Sonarly</span>
  <span class="partner"><i></i>Vantor</span>
</div>

<footer class="footer">
  <div class="fcol newsletter" style="left:99px;width:240px">
    <h4>NEWSLETTER</h4>
    <p>If you sign up the newsletter from NORTHPIXEL, you are sure never to miss Shopforge news again. We make sure to keep you updated on all sales and process promotion.</p>
    <form><span class="field">Enter Your E - Mail</span><span class="send">Sign Up</span></form>
  </div>
  <div class="fcol" style="left:391px;width:250px">
    <h4>LATEST TWEET`S</h4>
    <div class="tweet"><i></i><p>NORTHPIXEL now present our first Shopforge Template MrKestrel. See more here http://lnk.example/q7Rm2xK Price USD 25,000.00</p></div>
    <div class="tweet"><i></i><p>NORTHPIXEL now present our first Shopforge Template MrKestrel. See more here http://lnk.example/q7Rm2xK Price USD 25,000.00</p></div>
  </div>
  <div class="fcol" style="left:700px;width:260px">
    <h4>CONTACT US</h4>
    <ul class="contact-list">
      <li><svg width="12" height="16" viewBox="0 0 12 16"><path d="M6 0a6 6 0 0 0-6 6c0 4 6 10 6 10s6-6 6-10a6 6 0 0 0-6-6zm0 8.5A2.5 2.5 0 1 1 6 3.5a2.5 2.5 0 0 1 0 5z" fill="#888"/></svg><span>Address: Fluxbase Analytics, Elm Ridge 4B, 7110 Norbury</span></li>
      <li><svg width="14" height="14" viewBox="0 0 24 24"><path fill="none" stroke="#888" stroke-width="2" d="M6.6 10.8a15 15 0 0 0 6.6 6.6l2.2-2.2 4.6 1.3V20A17 17 0 0 1 4 4h3.5l1.3 4.6z"/></svg><span>Phone: +45 00 12 34 56</span></li>
      <li><svg width="16" height="12" viewBox="0 0 24 18"><rect x="1" y="1" width="22" height="16" fill="none" stroke="#888" stroke-width="2"/><path d="M1 1l11 9 11-9" fill="none" stroke="#888" stroke-width="2"/></svg><span>Email: hello@fluxbase.example</span></li>
    </ul>
  </div>
  <div class="fcol" style="left:989px;width:140px">
    <h4>SOCIAL MEDIA</h4>
    <ul class="social">
      <li><i></i>Friendwall</li>
      <li><i></i>Chirper</li>
      <li><i></i>Circleplus</li>
      <li><i></i>Viewtube</li>
    </ul>
  </div>
</footer>
<div class="bottombar">&copy;2013 - 2014 Fluxbase Analytics., All Rights Reserved.</div>

</body>
</html>
```